Design new RK Capital business card 2016

We need a new business card for our company RK Capital Stewardship. We are a niche Alternative Investment Fund Manager based in Chester, in the North West of the UK.We market our services to global institutions such as banks, insurance companies, pension funds, etc. as well as wealthy individuals. Our main markets are Europe (Germany\France\Switzerland), the US and parts of Asia.
The design needs to be in line with existing company branding. Life the assets we deal with, the business card might suggest, "niche\alternative" type of attributes - however, it needs to remain professional, clean and appropriate for our client base.
Our existing business card format with relevant factual information is included, along with logo and branding details.

Target Market(s)

We market our services to global institutions such as banks, insurance companies, pension funds, etc. as well as wealthy individuals.

Industry/Entity Type

Financial Service

Contact Information for Business Card

please see attached pdf for information on existing business card which we should aim to convey on your new design. However:
- the wording "RK Capital Stewardship Ltd is Authorised and Regulated
by the Monetary Oversight Bureau. Registered No. 7139604" should be replaced with , "RK Capital Stewardship Ltd is an Alternative Investment Fund Manager Authorised and Regulated by the Monetary Oversight Bureau. Registered No. 7139604"
- the "reception" word on reverse can be omitted.
- the "retail: www.marbowhill.co.uk" wording can be omitted.
- the QR code is not required in the new version.

Font styles to use
Serif
Sans Serif

Requirements
Must have
• information on current business card, subject to comments provided above.
Nice to have
• Use of areas of solid colour instead of large areas of white space might be nice to experiment with. However, still need to have the general look and feel of the brand as presented on our website www.rkcapfold.co.uk
• If we had space for 3 bullet points describing what we do\who we are, this might be good to try out. e.g. alternative investment fund manager, longevity specialist, founded 1990.
• Also, we have a new tag line, "wisdom built to endure" which might fit nicely somewhere on the business card.
Should not have
• - no QR code
• - should not use all the colours in our logo as it looks very garish! Using one or two colours with black\white etc, seems to work better.

```html
<!DOCTYPE html>
<html lang="en">
<head>
<meta charset="utf-8">
<title>RK Capital Stewardship – Business Card</title>
<link rel="stylesheet" href="https://fonts.googleapis.com/css2?family=Open+Sans:wght@400;600&display=swap">
<style>
  :root {
    --brown: #5e3608;
    --brown-text: #8a4b12;
    --gold: #f5b51b;
    --cyan: #29abe2;
    --olive: #a39a2a;
    --ink: #1a1a1a;
    --white: #ffffff;
    --backdrop: #e6e6e6;
    --tile-red: #e8222b;
    --tile-blue: #1da1e0;
    --tile-yellow: #f7b21c;
  }
  * { box-sizing: border-box; margin: 0; padding: 0; }
  html, body { width: 1200px; height: 903px; overflow: hidden; }
  body {
    background: var(--backdrop);
    font-family: "Open Sans", Arial, sans-serif;
    position: relative;
  }
  .card {
    position: absolute;
    width: 547px;
    height: 313px;
    background: var(--white);
    overflow: hidden;
    box-shadow: 4px 5px 8px rgba(0,0,0,0.35);
  }
  .card--front { left: 50px; top: 104px; }
  .card--back  { left: 580px; top: 321px; }

  /* decorative tile area */
  .tile-field {
    position: absolute;
    inset: 0;
    background:
      linear-gradient(135deg, var(--olive) 0%, var(--tile-red) 22%, transparent 40%),
      linear-gradient(45deg, var(--tile-blue) 0%, var(--tile-yellow) 18%, transparent 36%),
      linear-gradient(225deg, var(--olive) 0%, var(--tile-red) 14%, transparent 30%),
      linear-gradient(315deg, var(--tile-yellow) 0%, var(--tile-blue) 16%, transparent 32%);
  }
  .tile-field__clear {
    position: absolute;
    background: var(--white);
    border-radius: 50%;
  }

  /* front */
  .card--front .tile-field__clear { left: 28px; top: 14px; width: 520px; height: 290px; }
  .front__panel {
    position: absolute;
    left: 268px; top: 0; right: 0; bottom: 0;
    background: var(--brown);
    border-right: 5px solid #a55a12;
  }
  .front__name {
    position: absolute; right: 22px; top: 16px;
    color: var(--gold); font-size: 22px; font-weight: 400;
  }
  .front__title {
    position: absolute; right: 38px; top: 46px;
    color: var(--cyan); font-size: 18px;
  }
  .contact-list {
    position: absolute; right: 18px; bottom: 12px;
    list-style: none; color: var(--white); font-size: 19px; line-height: 30px;
    text-align: right;
  }
  .contact-list li { display: flex; align-items: center; justify-content: flex-end; gap: 8px; }
  .contact-list svg { width: 18px; height: 18px; flex: none; }

  .brand {
    position: absolute;
    display: flex; align-items: center; gap: 10px;
    color: var(--brown); font-size: 21px; font-weight: 600; line-height: 1.15;
  }
  .brand__dot { width: 16px; height: 16px; border-radius: 50%; background: var(--olive); flex: none; }
  .card--front .brand { left: 34px; top: 172px; width: 220px; }

  /* back */
  .card--back .tile-field__clear { left: 10px; top: 6px; width: 527px; height: 302px; }
  .back__notice {
    position: absolute; left: 0; right: 0; top: 16px;
    text-align: center; color: var(--ink); font-size: 16px; line-height: 22px;
  }
  .back__notice .lead { color: var(--brown-text); }
  .back__rule {
    position: absolute; left: 0; right: 0; top: 100px;
    height: 2px; background: var(--brown-text);
  }
  .card--back .brand { left: 40px; top: 190px; width: 210px; font-size: 20px; }
  .back__address {
    position: absolute; right: 26px; top: 140px;
    text-align: right; color: var(--ink); font-size: 16px; line-height: 23.5px;
    font-style: normal;
  }
  .back__address .company { color: var(--brown-text); }
</style>
</head>
<body>

<section class="card card--front" aria-label="Business card front">
  <div class="tile-field" role="img" aria-label="Decorative mosaic of coloured tiles around the card edges">
    <div class="tile-field__clear"></div>
  </div>
  <div class="brand"><span class="brand__dot"></span>RK Capital Stewardship</div>
  <div class="front__panel">
    <p class="front__name">Martin Hollis</p>
    <p class="front__title">Chief Executive</p>
    <ul class="contact-list">
      <li>
        <svg viewBox="0 0 18 18" aria-hidden="true"><circle cx="9" cy="9" r="8" fill="none" stroke="#f5b51b" stroke-width="1.5"/><path d="M6 5l2 2-1 1.2c.6 1.3 1.5 2.2 2.8 2.8L11 10l2 2-1.2 1.2C8.6 12.8 5.2 9.4 4.8 6.2z" fill="#f5b51b"/></svg>
        +44 (0) 1632960418
      </li>
      <li>
        <svg viewBox="0 0 18 18" aria-hidden="true"><circle cx="9" cy="9" r="8" fill="none" stroke="#f5b51b" stroke-width="1.5"/><rect x="6.5" y="4" width="5" height="10" rx="1" fill="none" stroke="#f5b51b" stroke-width="1.3"/></svg>
        +44 (0) 7700900613
      </li>
      <li>
        <svg viewBox="0 0 18 18" aria-hidden="true"><circle cx="9" cy="9" r="8" fill="none" stroke="#f5b51b" stroke-width="1.5"/><rect x="4.5" y="6" width="9" height="6.5" fill="none" stroke="#f5b51b" stroke-width="1.2"/><path d="M4.5 6l4.5 3.5L13.5 6" fill="none" stroke="#f5b51b" stroke-width="1.2"/></svg>
        mhollis@rkcapfold.co.uk
      </li>
    </ul>
  </div>
</section>

<section class="card card--back" aria-label="Business card back">
  <div class="tile-field" role="img" aria-label="Decorative mosaic of coloured tiles around the card edges">
    <div class="tile-field__clear"></div>
  </div>
  <p class="back__notice">
    <span class="lead">RK Capital Stewardship Ltd is an</span><br>
    Alternative Investment Fund Manager Authorised and Regulated<br>
    by the Monetary Oversight Bureau. Registered No. 7139604
  </p>
  <div class="back__rule"></div>
  <div class="brand"><span class="brand__dot"></span>RK Capital Stewardship</div>
  <address class="back__address">
    <span class="company">RK Capital Stewardship</span><br>
    14-16 Weaver Yard,<br>
    Tanner Street, Chester,<br>
    CH2 4QP, UK<br>
    +44 (0) 1632960227<br>
    Institutional: www.rkcapfold.co.uk
  </address>
</section>

</body>
</html>
```